Umgestaltung von Versandkartons
Zielgruppe
Vertrieb von fränkischen Bieren und Biergeschenksets.
Zielgruppe sind zum Teil Biergenießer, die etwas anderes trinken/probieren möchten und vor allem aber Menschen die ein Geschenk für zumeist Männer verschiedenen Alters suchen/kaufen.
Aufgabenstellung
Ich möchte meine Versandkartons umgestalten, sodass diese auch zugleich als Geschenkverpackung genutzt werden können. Das Markenlogo soll drauf und es darf auch mit den Deckelklappen gespielt werden. Also zB. ein witziger Spruch nach dem Umklappen des oberen Deckels, oder eine Grafik die Lust auf den Inhalt macht.
Zugleich sollte aber auch für die Paketboten ersichtlich sein, dass sich empfindliche Ware im Karton befindet, ohne dass der Empfänger/Beschenkte sofort sieht, was drin ist.
Ressourcenschonend sollte das Design auch sein, heisst ich möchte keine Hinterdrundfarbe drucken lassen(Materialfarbe ist Hintergrundfarbe).
Dateien mit Logo und Maße der 2 Kartons sind beigefügt.

```html
<!DOCTYPE html>
<html lang="de">
<head>
<meta charset="utf-8">
<title>Hopfenglück – Versandkarton Stanzbogen</title>
<link href="https://fonts.googleapis.com/css2?family=Barlow+Semi+Condensed:wght@500;600&family=Montserrat:wght@500;700&display=swap" rel="stylesheet">
<style>
  :root{
    --kraft:#b98c5f;
    --kraft-light:#c49a6c;
    --ink:#3b2a1f;
    --paper:#ffffff;
    --fold:#5a4230;
  }
  html,body{margin:0;padding:0;width:1200px;height:552px;overflow:hidden;background:var(--paper);}
  .dieline{position:relative;width:1200px;height:552px;font-family:"Montserrat",sans-serif;color:var(--ink);}
  .panel{position:absolute;background:linear-gradient(180deg,var(--kraft-light),var(--kraft) 60%,#b4875a);}
  .body-band{left:8px;top:211px;width:1148px;height:220px;border-top:1px solid var(--fold);}
  .fold-v{position:absolute;top:211px;height:220px;width:0;border-left:1px solid var(--fold);opacity:.55;}
  .glue-tab{position:absolute;left:1159px;top:211px;width:27px;height:220px;}
  .frame{position:absolute;inset:0;border:12.5px solid var(--ink);}
  .frame-text{position:absolute;color:var(--kraft-light);font-weight:700;font-size:11px;letter-spacing:4px;white-space:nowrap;line-height:1;}
  .rot{position:absolute;white-space:nowrap;transform:translate(-50%,-50%) rotate(-90deg);}
  .rot-down{position:absolute;white-space:nowrap;transform:translate(-50%,-50%) rotate(90deg);}
  .warning{font-size:5.5px;letter-spacing:2px;font-weight:500;}
  .tri{position:absolute;width:11px;height:11px;}
  .claim{font-size:11px;font-weight:700;letter-spacing:2.4px;line-height:1.25;}
  .url{font-size:11px;font-weight:700;letter-spacing:1.5px;}
  .tagline{position:absolute;font-size:14px;font-weight:500;letter-spacing:6.2px;white-space:nowrap;}
  .brand-name{position:absolute;font-family:"Barlow Semi Condensed",sans-serif;font-weight:600;font-size:46px;letter-spacing:9px;line-height:1;white-space:nowrap;}
  .brand-mark{position:absolute;display:flex;flex-direction:column;align-items:center;gap:6px;transform:translate(-50%,-50%);}
  .brand-mark .dot{width:44px;height:44px;border-radius:50%;background:var(--ink);}
  .brand-mark .word{font-family:"Barlow Semi Condensed",sans-serif;font-weight:600;font-size:15px;letter-spacing:2px;}
  .hop-art{position:absolute;left:457px;top:82px;width:34px;height:60px;background:radial-gradient(ellipse at 50% 45%,#4a382a,#7a5e43 60%,transparent 75%);}
  .fragile-icon{position:absolute;width:33px;height:32px;}
</style>
</head>
<body>
<div class="dieline">

  <!-- top flaps -->
  <div class="panel" style="left:8px;top:10px;width:365px;height:201px;">
    <div class="frame"></div>
    <div class="frame-text" style="left:50px;top:1px;">VORSICHT!&nbsp;&nbsp;&nbsp;ZERBRECHLICH!</div>
    <div class="frame-text" style="left:48px;bottom:1px;transform:rotate(180deg);">VORSICHT!&nbsp;&nbsp;&nbsp;ZERBRECHLICH!</div>
    <div class="frame-text rot" style="left:7px;top:110px;">ZERBRECHLICH!</div>
    <div class="frame-text rot-down" style="left:358px;top:110px;">VORSICHT!</div>
    <div class="brand-mark" style="left:183px;top:100px;"><span class="dot"></span><span class="word">HOPFENGLÜCK</span></div>
  </div>

  <div class="panel" style="left:379px;top:10px;width:200px;height:201px;">
    <svg class="tri" style="left:3px;top:10px;" viewBox="0 0 11 11"><path d="M1 1 L10 5.5 L1 10 Z" fill="none" stroke="var(--ink)"/></svg>
    <svg class="tri" style="left:3px;top:180px;" viewBox="0 0 11 11"><path d="M1 1 L10 5.5 L1 10 Z" fill="none" stroke="var(--ink)"/></svg>
    <svg class="tri" style="left:186px;top:10px;" viewBox="0 0 11 11"><path d="M10 1 L1 5.5 L10 10 Z" fill="none" stroke="var(--ink)"/></svg>
    <svg class="tri" style="left:186px;top:180px;" viewBox="0 0 11 11"><path d="M10 1 L1 5.5 L10 10 Z" fill="none" stroke="var(--ink)"/></svg>
    <div class="rot-down warning" style="left:9px;top:110px;">ACHTUNG!&nbsp;&nbsp;&nbsp;GENUSSGEFAHR!</div>
    <div class="rot warning" style="left:192px;top:110px;">ACHTUNG!&nbsp;&nbsp;&nbsp;GENUSSGEFAHR!</div>
    <div class="rot claim" style="left:67px;top:110px;">DER KONTRAST</div>
    <div class="rot claim" style="left:125px;top:105px;text-align:left;">MACHT DEN<br>GESCHMACK.</div>
    <div class="hop-art" style="left:78px;top:72px;" role="img" aria-label="Illustration eines Hopfenzweigs mit Dolden"></div>
  </div>

  <div class="panel" style="left:585px;top:10px;width:365px;height:201px;">
    <div class="tagline" style="left:51px;top:95px;">ETWAS BESONDERES.</div>
  </div>

  <div class="panel" style="left:956px;top:10px;width:200px;height:201px;">
    <svg class="tri" style="left:3px;top:10px;" viewBox="0 0 11 11"><path d="M1 1 L10 5.5 L1 10 Z" fill="none" stroke="var(--ink)"/></svg>
    <svg class="tri" style="left:3px;top:180px;" viewBox="0 0 11 11"><path d="M1 1 L10 5.5 L1 10 Z" fill="none" stroke="var(--ink)"/></svg>
    <svg class="tri" style="left:186px;top:10px;" viewBox="0 0 11 11"><path d="M10 1 L1 5.5 L10 10 Z" fill="none" stroke="var(--ink)"/></svg>
    <svg class="tri" style="left:186px;top:180px;" viewBox="0 0 11 11"><path d="M10 1 L1 5.5 L10 10 Z" fill="none" stroke="var(--ink)"/></svg>
    <div class="rot-down warning" style="left:9px;top:110px;">ACHTUNG!&nbsp;&nbsp;&nbsp;GENUSSGEFAHR!</div>
    <div class="rot warning" style="left:192px;top:110px;">ACHTUNG!&nbsp;&nbsp;&nbsp;GENUSSGEFAHR!</div>
    <div class="rot-down url" style="left:96px;top:110px;">HOPFENGLUECK.DE</div>
  </div>

  <!-- body panels -->
  <div class="panel body-band"></div>
  <div class="fold-v" style="left:583px;"></div>
  <svg class="glue-tab" viewBox="0 0 27 220" preserveAspectRatio="none"><path d="M0 0 L27 7 L27 213 L0 220 Z" fill="var(--kraft)" stroke="var(--fold)" stroke-width=".6"/></svg>

  <div class="brand-name" style="left:58px;top:290px;">HOPFENGLÜCK</div>
  <div class="tagline" style="left:61px;top:345px;">ETWAS BESONDERES.</div>
  <div class="brand-mark" style="left:478px;top:320px;"><span class="dot"></span><span class="word">HOPFENGLÜCK</span></div>

  <div class="brand-name" style="left:634px;top:290px;">HOPFENGLÜCK</div>
  <div class="tagline" style="left:636px;top:345px;">ETWAS BESONDERES.</div>
  <div class="brand-mark" style="left:1052px;top:320px;"><span class="dot"></span><span class="word">HOPFENGLÜCK</span></div>

  <svg class="fragile-icon" style="left:384px;top:392px;" viewBox="0 0 33 32">
    <rect x="1" y="1" width="31" height="30" fill="none" stroke="var(--ink)" stroke-width="1.6"/>
    <path d="M11 6 H22 V12 Q22 17 16.5 17 Q11 17 11 12 Z" fill="var(--ink)"/>
    <rect x="15.8" y="17" width="1.4" height="7" fill="var(--ink)"/>
    <rect x="12" y="24" width="9" height="1.6" fill="var(--ink)"/>
  </svg>
  <svg class="fragile-icon" style="left:962px;top:392px;" viewBox="0 0 33 32">
    <rect x="1" y="1" width="31" height="30" fill="none" stroke="var(--ink)" stroke-width="1.6"/>
    <path d="M11 6 H22 V12 Q22 17 16.5 17 Q11 17 11 12 Z" fill="var(--ink)"/>
    <rect x="15.8" y="17" width="1.4" height="7" fill="var(--ink)"/>
    <rect x="12" y="24" width="9" height="1.6" fill="var(--ink)"/>
  </svg>

  <!-- bottom flaps -->
  <div class="panel" style="left:8px;top:431px;width:365px;height:103px;"></div>
  <div class="panel" style="left:379px;top:431px;width:200px;height:103px;"></div>
  <div class="panel" style="left:585px;top:431px;width:365px;height:103px;"></div>
  <div class="panel" style="left:956px;top:431px;width:200px;height:103px;"></div>

</div>
</body>
</html>
```